Need Powerpoint masters for my consulting company in privacy (RGPD) and IT

For my newly created consulting company I need powerpoint slides masters.
The company is specialzed in privacy (RGPD) and IT.
The company already has a logo (obtained via Pixelhive).
These master slides will be mainly used when presenting reports/analysis to clients.
I'll attach a PNG files of the logo.

```html
<!DOCTYPE html>
<html lang="en">
<head>
<meta charset="utf-8">
<title>Duvernet Conseil – Presentation Masters</title>
<link href="https://fonts.googleapis.com/css2?family=Montserrat:wght@500;600;700;800&family=Open+Sans:wght@400;600;700&display=swap" rel="stylesheet">
<style>
:root{
  --canvas:#c5c5c7;
  --navy:#0c2d48;
  --teal:#0f8795;
  --teal-dark:#0a5b6b;
  --teal-deep:#083f55;
  --grey:#525458;
  --ink:#3b3e43;
  --muted:#8a8d92;
  --line:#d6d8db;
  --white:#ffffff;
}
*{box-sizing:border-box}
html,body{margin:0;padding:0}
body{width:1200px;height:3344px;overflow:hidden;background:var(--canvas);position:relative;font-family:'Open Sans',sans-serif;color:var(--ink)}
.slide{position:absolute;width:960px;height:540px;background:var(--white);overflow:hidden;transform-origin:0 0;transform:scale(.5625)}
.slide.hero{transform:scale(.784)}
.abs{position:absolute}
.fill{position:absolute;left:0;top:0;width:100%;height:100%}
.date-line{position:absolute;left:78px;top:50px;font-size:13px;font-weight:600;color:var(--ink);letter-spacing:.3px}
.date-line b{color:var(--teal);font-weight:700;margin-right:8px}
.date-line span{border-left:1px solid var(--muted);padding-left:8px}
.cover-title{position:absolute;left:78px;top:172px;font-family:'Montserrat',sans-serif;font-weight:800;font-size:56px;line-height:60px;color:var(--white);letter-spacing:-1px}
.cover-sub{position:absolute;left:78px;top:306px;font-size:28px;line-height:32px;color:var(--white)}
.cover-copy{position:absolute;left:78px;top:477px;font-size:10px;color:var(--ink)}
.brand{position:absolute;font-family:'Montserrat',sans-serif;font-weight:600;color:var(--teal-dark);text-align:center;letter-spacing:1px}
.brand small{display:block;font-size:.42em;letter-spacing:9px;margin-top:6px}
.brand::before{content:"";display:block;width:34px;height:34px;margin:0 auto 12px;background:currentColor}
.slide-title{position:absolute;left:56px;top:48px;font-family:'Montserrat',sans-serif;font-weight:500;font-size:38px;color:var(--teal);letter-spacing:-.5px}
.slide-title::after{content:"";display:block;width:96px;height:2px;background:var(--line);margin-top:8px}
.slide-title.light{color:var(--white)}
.slide-title.light::after{background:rgba(255,255,255,.5)}
.foot{position:absolute;left:0;bottom:0;width:960px;height:70px}
.foot-brand{position:absolute;left:12px;bottom:16px;font-family:'Montserrat',sans-serif;font-weight:600;font-size:12px;color:var(--white);letter-spacing:.5px}
.foot-copy{position:absolute;right:22px;bottom:4px;font-size:8px;color:var(--white)}
.body-text{font-size:15px;line-height:17px;color:var(--ink)}
.toc-item{position:absolute;width:330px}
.toc-num{position:absolute;left:-44px;top:4px;font-family:'Montserrat',sans-serif;font-size:34px;color:#9a9da1}
.toc-head{font-family:'Montserrat',sans-serif;font-weight:600;font-size:21px;color:var(--teal)}
.toc-head span{font-weight:500}
.toc-text{font-size:12px;line-height:14px;color:var(--ink)}
.col-head{font-family:'Montserrat',sans-serif;font-weight:600;font-size:24px;color:var(--teal);margin-bottom:16px}
.bullets{margin:0;padding-left:18px;font-size:15px;line-height:17px;color:var(--ink)}
.bullets li{margin-bottom:12px}
.bullets li::marker{color:var(--teal)}
.section-title{position:absolute;left:76px;top:305px;font-family:'Montserrat',sans-serif;font-weight:700;font-size:54px;letter-spacing:-1px}
.section-sub{position:absolute;left:78px;top:390px;font-size:25px}
.section-name{position:absolute;left:76px;top:215px;font-family:'Montserrat',sans-serif;font-weight:600;font-size:26px;display:flex;align-items:center;gap:12px}
.section-name::before{content:"";width:40px;height:40px;background:currentColor}
.ring-card{position:absolute;width:200px;text-align:center}
.ring-head{font-family:'Montserrat',sans-serif;font-weight:700;font-size:17px;line-height:19px;color:var(--navy);margin-top:6px}
.ring-text{font-size:11.5px;line-height:13px;color:var(--ink);margin-top:8px;padding:0 46px}
.list-row{position:absolute;left:72px;display:flex;align-items:center;gap:28px;width:430px}
.list-row p{margin:0;font-size:12px;line-height:13px;color:var(--ink)}
.dot-icon{width:32px;height:32px;flex:none}
.card{position:absolute;top:150px;width:240px;height:238px;border-radius:10px;padding:18px 20px 0 18px;border:3px solid var(--white);box-shadow:0 2px 6px rgba(0,0,0,.25)}
.card ul{margin:0;padding-left:16px;font-size:13px;line-height:14.5px;color:var(--white)}
.card li{margin-bottom:10px}
.card-head{position:absolute;top:408px;width:240px;text-align:center;font-family:'Montserrat',sans-serif;font-weight:500;font-size:22px}
.data-table{border-collapse:collapse;width:100%;font-size:12px}
.data-table th{background:var(--navy);color:var(--white);text-align:left;padding:5px 8px;font-weight:700}
.data-table th:first-child{background:var(--teal)}
.data-table td{padding:4px 8px;border-bottom:1px solid #e3e5e7;color:var(--ink)}
.legend-row{position:absolute;left:585px;width:320px}
.legend-row h4{margin:0 0 6px;font-family:'Montserrat',sans-serif;font-weight:600;font-size:18px;display:flex;align-items:center;gap:14px}
.legend-row h4::before{content:"";width:18px;height:18px;background:currentColor;flex:none}
.legend-row p{margin:0 0 0 32px;font-size:11.5px;line-height:13px;color:var(--ink)}
.donut{position:absolute;width:200px;text-align:center}
.donut-head{font-family:'Montserrat',sans-serif;font-weight:500;font-size:24px;color:var(--ink);margin-top:10px}
.donut-text{font-size:12px;line-height:13px;color:var(--ink);padding:0 20px;margin-top:6px}
.donut-value{position:absolute;left:0;top:86px;width:200px;text-align:center;font-family:'Montserrat',sans-serif;font-weight:600;font-size:38px}
.donut-value span{font-size:22px}
.grid-table{position:absolute;left:65px;top:130px;width:831px;border-collapse:collapse;font-size:12.5px}
.grid-table th{background:var(--teal);color:var(--white);padding:12px 10px;font-weight:600;text-align:center;font-size:15px}
.grid-table th:first-child{background:var(--navy);text-align:left}
.grid-table td{padding:15px 10px;text-align:center;color:var(--ink);background:#eef0f2;border-bottom:3px solid var(--white)}
.grid-table td:first-child{text-align:left;font-weight:700;color:var(--navy);background:#e2e5e8}
.grid-table td:nth-child(2){background:#d8dcdf}
.contact{position:absolute;left:536px;top:205px;color:var(--white)}
.contact h3{margin:0 0 26px;font-family:'Montserrat',sans-serif;font-weight:600;font-size:21px}
.contact p{margin:0 0 16px;font-size:15px;display:flex;align-items:center;gap:16px}
.contact svg{width:18px;height:18px;flex:none}
</style>
</head>
<body>

<svg width="0" height="0" style="position:absolute" aria-hidden="true">
  <defs>
    <linearGradient id="footGrad" x1="0" x2="1">
      <stop offset="0" stop-color="#0c3a55"/><stop offset=".5" stop-color="#0f8795"/><stop offset="1" stop-color="#0c4a62"/>
    </linearGradient>
    <linearGradient id="tealPhoto" x1="0" y1="0" x2="1" y2="1">
      <stop offset="0" stop-color="#0f8795"/><stop offset=".6" stop-color="#137a88"/><stop offset="1" stop-color="#2f6f7c"/>
    </linearGradient>
    <linearGradient id="paleWork" x1="0" y1="0" x2="1" y2="1">
      <stop offset="0" stop-color="#e7ecef"/><stop offset=".6" stop-color="#cfd9df"/><stop offset="1" stop-color="#b9c7cf"/>
    </linearGradient>
    <linearGradient id="deepBand" x1="0" y1="0" x2="1" y2="1">
      <stop offset="0" stop-color="#0f8795"/><stop offset="1" stop-color="#0a3450"/>
    </linearGradient>
    <linearGradient id="handsPhoto" x1="0" y1="0" x2="1" y2="1">
      <stop offset="0" stop-color="#23435c"/><stop offset=".5" stop-color="#6c8ea5"/><stop offset="1" stop-color="#c9d6df"/>
    </linearGradient>
  </defs>
</svg>

<!-- Cover, large -->
<section class="slide hero" style="left:225px;top:90px">
  <div class="date-line"><b>NOW</b><span>MONDAY, OCTOBER 18, 2021</span></div>
  <svg class="fill" viewBox="0 0 960 540">
    <polygon role="img" aria-label="Photo of a team working at laptops, seen from above, in teal tones" points="0,119 550,119 630,58 960,58 960,353 634,353 526,413 0,413" fill="url(#tealPhoto)"/>
    <polygon points="0,419 528,419 636,359 960,359 960,366 640,366 532,428 0,428" fill="var(--navy)"/>
  </svg>
  <div class="cover-title">Presentation<br>Title Goes Here!</div>
  <div class="cover-sub">Subtitle of Presentation<br>Goes Here!</div>
  <div class="cover-copy">Copyright 2021 Duvernet Conseil. All rights reserved</div>
  <div class="brand" style="left:620px;top:385px;width:290px;font-size:26px">Duvernet<small>CONSEIL</small></div>
</section>

<!-- Cover, white -->
<section class="slide" style="left:52px;top:737px">
  <div class="date-line"><b>NOW</b><span>MONDAY, OCTOBER 18, 2021</span></div>
  <svg class="fill" viewBox="0 0 960 540">
    <polygon role="img" aria-label="Photo of a team working at laptops, seen from above, in teal tones" points="0,119 550,119 630,58 960,58 960,353 634,353 526,413 0,413" fill="url(#tealPhoto)"/>
    <polygon points="0,419 528,419 636,359 960,359 960,366 640,366 532,428 0,428" fill="var(--navy)"/>
  </svg>
  <div class="cover-title">Presentation<br>Title Goes Here!</div>
  <div class="cover-sub">Subtitle of Presentation<br>Goes Here!</div>
  <div class="cover-copy">Copyright 2021 Duvernet Conseil. All rights reserved</div>
  <div class="brand" style="left:620px;top:385px;width:290px;font-size:26px">Duvernet<small>CONSEIL</small></div>
</section>

<!-- Cover, dark -->
<section class="slide" style="left:610px;top:737px">
  <svg class="fill" viewBox="0 0 960 540">
    <rect role="img" aria-label="Bright photo of hands using a tablet over documents" width="960" height="540" fill="url(#paleWork)"/>
    <polygon points="0,0 960,0 960,58 640,58 580,118 0,118" fill="url(#deepBand)"/>
    <polygon points="0,411 520,411 628,345 960,345 960,540 0,540" fill="url(#deepBand)"/>
    <polygon points="0,402 516,402 624,336 960,336 960,342 627,342 519,408 0,408" fill="var(--navy)"/>
  </svg>
  <div class="date-line" style="color:#fff"><b style="color:#fff">NOW</b><span>MONDAY, OCTOBER 18, 2021</span></div>
  <div class="cover-title" style="color:var(--navy)">Presentation<br>Title Goes Here!</div>
  <div class="cover-sub" style="color:var(--teal)">Subtitle of Presentation<br>Goes Here!</div>
  <div class="cover-copy" style="color:#fff">Copyright 2021 Duvernet Conseil. All rights reserved</div>
  <div class="brand" style="left:620px;top:385px;width:290px;font-size:26px;color:#fff">Duvernet<small>CONSEIL</small></div>
</section>

<!-- Table of content -->
<section class="slide" style="left:52px;top:1060px">
  <div class="slide-title" style="top:50px">Table of Content</div>
  <div class="toc-item" style="left:180px;top:170px"><div class="toc-num">1</div><div class="toc-head">Title <span>Goes Here!</span></div><div class="toc-text">Lorem ipsum dolor sit amet, consectetur<br>adipiscing elit. Vivamus eu dui ex.</div></div>
  <div class="toc-item" style="left:561px;top:170px"><div class="toc-num">2</div><div class="toc-head">Title <span>Goes Here!</span></div><div class="toc-text">Lorem ipsum dolor sit amet, consectetur<br>adipiscing elit. Vivamus eu dui ex.</div></div>
  <div class="toc-item" style="left:180px;top:265px"><div class="toc-num">3</div><div class="toc-head">Title <span>Goes Here!</span></div><div class="toc-text">Lorem ipsum dolor sit amet, consectetur<br>adipiscing elit. Vivamus eu dui ex.</div></div>
  <div class="toc-item" style="left:561px;top:265px"><div class="toc-num">4</div><div class="toc-head">Title <span>Goes Here!</span></div><div class="toc-text">Lorem ipsum dolor sit amet, consectetur<br>adipiscing elit. Vivamus eu dui ex.</div></div>
  <div class="toc-item" style="left:180px;top:360px"><div class="toc-num">5</div><div class="toc-head">Title <span>Goes Here!</span></div><div class="toc-text">Lorem ipsum dolor sit amet, consectetur<br>adipiscing elit. Vivamus eu dui ex.</div></div>
  <div class="toc-item" style="left:561px;top:360px"><div class="toc-num">6</div><div class="toc-head">Title <span>Goes Here!</span></div><div class="toc-text">Lorem ipsum dolor sit amet, consectetur<br>adipiscing elit. Vivamus eu dui ex.</div></div>
  <svg class="foot" viewBox="0 0 960 70"><polygon points="0,12 112,12 156,56 960,56 960,70 0,70" fill="url(#footGrad)"/></svg>
  <div class="foot-brand">Duvernet</div><div class="foot-copy">Copyright 2021 Duvernet Conseil. All rights reserved &nbsp;|&nbsp; 3</div>
</section>

<!-- Photo + text -->
<section class="slide" style="left:610px;top:1060px">
  <svg class="abs" style="left:46px;top:0" width="421" height="400"><rect role="img" aria-label="Photo of hands holding a tablet showing a bar chart" width="421" height="400" fill="url(#handsPhoto)"/></svg>
  <div class="abs" style="left:513px;top:48px;font-family:'Montserrat',sans-serif;font-weight:600;font-size:36px;line-height:40px;color:var(--teal)">Slide Title<br><span style="font-weight:500">Goes Here!</span></div>
  <div class="abs body-text" style="left:513px;top:170px;width:400px;font-size:13px;line-height:14px">Lorem ipsum dolor sit amet, consectetur adipiscing elit. Vivamus eu dui ex. Curabitur dapibus dignissim dui, in molestie metus feugiat sed. Praesent aliquet lorem ex, eu dapibus odio varius at. Duis eget tellus porta, consequat lacus vitae, venenatis dolor.<br><br>Nulla facilisi. In et sollicitudin lacus. Donec risus orci, gravida sit amet risus vehicula, aliquet pretium sapien. Nullam sit amet magna non ex bibendum mollis. Nunc vel neque eu augue dignissim congue ut vitae magna. Phasellus eget commodo arcu. Nunc vitae semper dui. Integer venenatis, tellus sit amet interdum pretium, erat neque rhoncus turpis, a aliquam augue ligula eget erat. Nunc placerat, arcu nec mattis fermentum, nisi mauris convallis nunc.</div>
  <svg class="foot" viewBox="0 0 960 70"><polygon points="0,12 112,12 156,56 960,56 960,70 0,70" fill="url(#footGrad)"/></svg>
  <div class="foot-brand">Duvernet</div><div class="foot-copy">Copyright 2021 Duvernet Conseil. All rights reserved &nbsp;|&nbsp; 4</div>
</section>

<!-- Two columns -->
<section class="slide" style="left:52px;top:1382px">
  <div class="slide-title">Slide Title Goes Here!</div>
  <div class="abs" style="left:72px;top:162px;width:370px"><div class="col-head">Title Goes Here</div>
    <ul class="bullets"><li>Lorem ipsum dolor sit amet, at laborum nibh duis mauris. Per ultrices lectus sed metus tristique eu.</li><li>Diam suspendisse ac ipsum maecenas fermentum, aliquet imperdiet et lobortis venenatis nascetur lacus.</li><li>A ac, vivamus erat nullam. Lorem ipsum dolor sit amet, at laborum nibh duis mauris. Per ultrices lectus sed metus tristique eu. Diam suspendisse.</li></ul></div>
  <div class="abs" style="left:506px;top:162px;width:370px"><div class="col-head">Title Goes Here</div>
    <ul class="bullets"><li>Lorem ipsum dolor sit amet, at laborum nibh duis mauris. Per ultrices lectus sed metus tristique eu.</li><li>Diam suspendisse ac ipsum maecenas fermentum, aliquet imperdiet et lobortis venenatis nascetur lacus.</li><li>A ac, vivamus erat nullam. Lorem ipsum dolor sit amet, at laborum nibh duis mauris. Per ultrices lectus sed metus tristique eu. Diam suspendisse.</li></ul></div>
  <svg class="foot" viewBox="0 0 960 70"><polygon points="0,12 112,12 156,56 960,56 960,70 0,70" fill="url(#footGrad)"/></svg>
  <div class="foot-brand">Duvernet</div><div class="foot-copy">Copyright 2021 Duvernet Conseil. All rights reserved &nbsp;|&nbsp; 5</div>
</section>

<!-- Section break, teal -->
<section class="slide" style="left:610px;top:1382px;background:var(--teal)">
  <svg class="fill" viewBox="0 0 960 540"><rect role="img" aria-label="Photo of hands using a tablet, tinted teal" width="960" height="540" fill="url(#tealPhoto)"/></svg>
  <div class="section-name" style="color:#fff">Duvernet</div>
  <div class="section-title" style="color:#fff">Section Break</div>
  <div class="section-sub" style="color:#fff">Subtitle of Section Break Goes Here!</div>
</section>

<!-- Four rings -->
<section class="slide" style="left:52px;top:1704px">
  <div class="slide-title">Slide Title Goes Here!</div>
  <svg class="abs" style="left:0;top:0" width="960" height="540" viewBox="0 0 960 540" aria-hidden="true">
    <g fill="none" stroke-width="9">
      <path d="M98,262 A85,85 0 0 1 258,262 M258,320 A85,85 0 0 1 98,320" stroke="var(--navy)"/>
      <path d="M299,262 A85,85 0 0 1 459,262 M459,320 A85,85 0 0 1 299,320" stroke="var(--teal)"/>
      <path d="M500,262 A85,85 0 0 1 660,262 M660,320 A85,85 0 0 1 500,320" stroke="var(--grey)"/>
      <path d="M701,262 A85,85 0 0 1 861,262 M861,320 A85,85 0 0 1 701,320" stroke="#111"/>
    </g>
    <circle cx="178" cy="222" r="30" fill="var(--navy)"/>
    <circle cx="178" cy="217" r="9" fill="#fff"/><rect x="173" y="225" width="10" height="9" rx="2" fill="#fff"/>
    <circle cx="379" cy="222" r="30" fill="var(--teal)"/>
    <path d="M369,232 L389,206 L392,213 L374,236 Z M366,228 l6,-2 -2,6 z" fill="#fff"/>
    <circle cx="580" cy="222" r="30" fill="var(--grey)"/>
    <circle cx="580" cy="222" r="13" fill="none" stroke="#fff" stroke-width="6" stroke-dasharray="4 3"/><circle cx="580" cy="222" r="5" fill="#fff"/>
    <circle cx="781" cy="222" r="30" fill="#111"/>
    <circle cx="781" cy="214" r="8" fill="#fff"/><path d="M767,236 a14,12 0 0 1 28,0 z" fill="#fff"/>
  </svg>
  <div class="ring-card" style="left:78px;top:270px"><div class="ring-head">Title Goes<br>Here!</div><div class="ring-text">Lorem ipsum dolor sit amet, consectetur adipiscing elit. Vivamus eu dui ex. Curabitur.</div></div>
  <div class="ring-card" style="left:279px;top:270px"><div class="ring-head" style="color:var(--teal)">Title Goes<br>Here!</div><div class="ring-text">Lorem ipsum dolor sit amet, consectetur adipiscing elit. Vivamus eu dui ex. Curabitur.</div></div>
  <div class="ring-card" style="left:480px;top:270px"><div class="ring-head" style="color:var(--grey)">Title Goes<br>Here!</div><div class="ring-text">Lorem ipsum dolor sit amet, consectetur adipiscing elit. Vivamus eu dui ex. Curabitur.</div></div>
  <div class="ring-card" style="left:681px;top:270px"><div class="ring-head" style="color:#111">Title Goes<br>Here!</div><div class="ring-text">Lorem ipsum dolor sit amet, consectetur adipiscing elit. Vivamus eu dui ex. Curabitur.</div></div>
  <svg class="foot" viewBox="0 0 960 70"><polygon points="0,12 112,12 156,56 960,56 960,70 0,70" fill="url(#footGrad)"/></svg>
  <div class="foot-brand">Duvernet</div><div class="foot-copy">Copyright 2021 Duvernet Conseil. All rights reserved &nbsp;|&nbsp; 7</div>
</section>

<!-- Icon list + photo -->
<section class="slide" style="left:610px;top:1704px">
  <div class="slide-title">Slide Title Goes Here!</div>
  <svg class="abs" style="left:545px;top:0" width="361" height="437"><rect role="img" aria-label="Photo of hands holding a tablet showing a bar chart" width="361" height="437" fill="url(#handsPhoto)"/></svg>
  <div class="list-row" style="top:141px"><svg class="dot-icon" viewBox="0 0 32 32"><circle cx="16" cy="16" r="16" fill="var(--navy)"/><circle cx="16" cy="13" r="5" fill="#fff"/><rect x="13" y="18" width="6" height="5" fill="#fff"/></svg><p>Lorem ipsum dolor sit amet, at laborum nibh duis mauris. Per ultrices lectus sed metus tristique eu.</p></div>
  <div class="list-row" style="top:217px"><svg class="dot-icon" viewBox="0 0 32 32"><circle cx="16" cy="16" r="16" fill="var(--teal)"/><path d="M10,22 L21,9 L23,12 L13,24 Z" fill="#fff"/></svg><p>Lorem ipsum dolor sit amet, at laborum nibh duis mauris. Per ultrices lectus sed metus tristique eu.</p></div>
  <div class="list-row" style="top:296px"><svg class="dot-icon" viewBox="0 0 32 32"><circle cx="16" cy="16" r="16" fill="var(--grey)"/><circle cx="16" cy="16" r="7" fill="none" stroke="#fff" stroke-width="3" stroke-dasharray="3 2"/></svg><p>Lorem ipsum dolor sit amet, at laborum nibh duis mauris. Per ultrices lectus sed metus tristique eu.</p></div>
  <div class="list-row" style="top:372px"><svg class="dot-icon" viewBox="0 0 32 32"><circle cx="16" cy="16" r="16" fill="#111"/><circle cx="16" cy="12" r="5" fill="#fff"/><path d="M8,25 a8,7 0 0 1 16,0 z" fill="#fff"/></svg><p>Lorem ipsum dolor sit amet, at laborum nibh duis mauris. Per ultrices lectus sed metus tristique eu.</p></div>
  <svg class="foot" viewBox="0 0 960 70"><polygon points="0,12 112,12 156,56 960,56 960,70 0,70" fill="url(#footGrad)"/></svg>
  <div class="foot-brand">Duvernet</div><div class="foot-copy">Copyright 2021 Duvernet Conseil. All rights reserved &nbsp;|&nbsp; 8</div>
</section>

<!-- Three cards -->
<section class="slide" style="left:52px;top:2025px">
  <svg class="fill" viewBox="0 0 960 540"><polygon role="img" aria-label="Photo of a team working at desks, tinted teal" points="0,0 960,0 960,190 0,190" fill="url(#tealPhoto)"/></svg>
  <div class="slide-title light">Slide Title <span style="font-weight:500">Goes Here!</span></div>
  <div class="card" style="left:88px;background:var(--navy)"><ul><li>Lorem ipsum dolor sit amet, consectetur adipiscing elit. Vivamus eu dui ex.</li><li>Curabitur dapibus dignissim dui, in molestie metus feugiat sed.</li><li>Praesent aliquet lorem ex, eu dapibus odio varius at.</li><li>Duis eget tellus porta, consequat lacus vitae, venenatis dolor.</li></ul></div>
  <div class="card" style="left:360px;background:var(--teal)"><ul><li>Lorem ipsum dolor sit amet, consectetur adipiscing elit. Vivamus eu dui ex.</li><li>Curabitur dapibus dignissim dui, in molestie metus feugiat sed.</li><li>Praesent aliquet lorem ex, eu dapibus odio varius at.</li><li>Duis eget tellus porta, consequat lacus vitae, venenatis dolor.</li></ul></div>
  <div class="card" style="left:632px;background:var(--grey)"><ul><li>Lorem ipsum dolor sit amet, consectetur adipiscing elit. Vivamus eu dui ex.</li><li>Curabitur dapibus dignissim dui, in molestie metus feugiat sed.</li><li>Praesent aliquet lorem ex, eu dapibus odio varius at.</li><li>Duis eget tellus porta, consequat lacus vitae, venenatis dolor.</li></ul></div>
  <div class="card-head" style="left:88px;color:var(--ink)">Heading 1</div>
  <div class="card-head" style="left:360px;color:var(--teal)">Heading 2</div>
  <div class="card-head" style="left:632px;color:var(--grey)">Heading 3</div>
  <svg class="foot" viewBox="0 0 960 70"><polygon points="0,12 112,12 156,56 960,56 960,70 0,70" fill="url(#footGrad)"/></svg>
  <div class="foot-brand">Duvernet</div><div class="foot-copy">Copyright 2021 Duvernet Conseil. All rights reserved &nbsp;|&nbsp; 9</div>
</section>

<!-- Section break, light -->
<section class="slide" style="left:610px;top:2025px">
  <svg class="fill" viewBox="0 0 960 540"><rect role="img" aria-label="Pale photo of a team meeting around a table, seen from above" width="960" height="540" fill="url(#paleWork)" opacity=".6"/></svg>
  <div class="section-name" style="color:var(--navy)">Duvernet</div>
  <div class="section-title" style="color:var(--navy)">Section Break</div>
  <div class="section-sub" style="color:var(--teal)">Subtitle of Section Break Goes Here!</div>
</section>

<!-- Column chart + table -->
<section class="slide" style="left:52px;top:2348px">
  <div class="slide-title">Slide Title <span style="font-weight:400">Goes Here!</span></div>
  <svg class="abs" style="left:70px;top:150px" width="400" height="250" viewBox="0 0 400 250" aria-label="Column chart of three series across six categories">
    <g font-size="8" fill="#777" text-anchor="end">
      <text x="18" y="25">6</text><text x="18" y="58">5</text><text x="18" y="91">4</text><text x="18" y="124">3</text><text x="18" y="157">2</text><text x="18" y="190">1</text><text x="18" y="223">0</text>
    </g>
    <line x1="28" y1="220" x2="392" y2="220" stroke="#ccc"/>
    <g>
      <rect x="40" y="78" width="12" height="142" fill="var(--navy)"/><rect x="54" y="141" width="12" height="79" fill="var(--teal)"/><rect x="68" y="154" width="12" height="66" fill="var(--grey)"/>
      <rect x="98" y="138" width="12" height="82" fill="var(--navy)"/><rect x="112" y="75" width="12" height="145" fill="var(--teal)"/><rect x="126" y="154" width="12" height="66" fill="var(--grey)"/>
      <rect x="156" y="104" width="12" height="116" fill="var(--navy)"/><rect x="170" y="161" width="12" height="59" fill="var(--teal)"/><rect x="184" y="121" width="12" height="99" fill="var(--grey)"/>
      <rect x="214" y="72" width="12" height="148" fill="var(--navy)"/><rect x="228" y="128" width="12" height="92" fill="var(--teal)"/><rect x="242" y="55" width="12" height="165" fill="var(--grey)"/>
      <rect x="272" y="78" width="12" height="142" fill="var(--navy)"/><rect x="286" y="141" width="12" height="79" fill="var(--teal)"/><rect x="300" y="154" width="12" height="66" fill="var(--grey)"/>
      <rect x="330" y="138" width="12" height="82" fill="var(--navy)"/><rect x="344" y="75" width="12" height="145" fill="var(--teal)"/><rect x="358" y="154" width="12" height="66" fill="var(--grey)"/>
    </g>
    <g font-size="8" fill="#777" text-anchor="middle">
      <text x="60" y="234">Category 1</text><text x="118" y="234">Category 2</text><text x="176" y="234">Category 3</text><text x="234" y="234">Category 4</text><text x="292" y="234">Category 5</text><text x="350" y="234">Category 6</text>
    </g>
  </svg>
  <div class="abs" style="left:494px;top:150px;width:410px;font-size:12px;line-height:13px">Lorem ipsum dolor sit amet, at laborum nibh duis mauris. Per ultrices lectus sed metus tristique eu. Diam suspendisse ac ipsum maecenas fermentum, aliquet imperdiet et lobortis venenatis nascetur lacus. A ac, vivamus erat nullam.</div>
  <div class="abs" style="left:487px;top:240px;width:416px">
    <table class="data-table"><tr><th>Category</th><th>Series 1</th><th>Series 2</th><th>Series 3</th></tr>
      <tr><td>Category 1</td><td>4.3</td><td>2.4</td><td>2</td></tr><tr><td>Category 2</td><td>2.5</td><td>4.4</td><td>2</td></tr><tr><td>Category 3</td><td>3.5</td><td>1.8</td><td>3</td></tr><tr><td>Category 4</td><td>4.5</td><td>2.8</td><td>5</td></tr><tr><td>Category 5</td><td>4.3</td><td>2.4</td><td>2</td></tr><tr><td>Category 6</td><td>2.5</td><td>4.4</td><td>2</td></tr></table>
  </div>
  <svg class="foot" viewBox="0 0 960 70"><polygon points="0,12 112,12 156,56 960,56 960,70 0,70" fill="url(#footGrad)"/></svg>
  <div class="foot-brand">Duvernet</div><div class="foot-copy">Copyright 2021 Duvernet Conseil. All rights reserved &nbsp;|&nbsp; 11</div>
</section>

<!-- Bar chart + legend -->
<section class="slide" style="left:610px;top:2348px">
  <div class="slide-title">Slide Title Goes Here!</div>
  <svg class="abs" style="left:80px;top:150px" width="470" height="270" viewBox="0 0 470 270" aria-label="Horizontal bar chart of three series across four categories">
    <g font-size="8" fill="#777" text-anchor="end"><text x="44" y="38">Category 4</text><text x="44" y="98">Category 3</text><text x="44" y="158">Category 2</text><text x="44" y="218">Category 1</text></g>
    <line x1="54" y1="10" x2="54" y2="245" stroke="#ccc"/>
    <rect x="54" y="24" width="320" height="9" fill="var(--grey)"/><rect x="54" y="33" width="179" height="9" fill="var(--teal)"/><rect x="54" y="42" width="288" height="9" fill="var(--navy)"/>
    <rect x="54" y="84" width="192" height="9" fill="var(--grey)"/><rect x="54" y="93" width="115" height="9" fill="var(--teal)"/><rect x="54" y="102" width="224" height="9" fill="var(--navy)"/>
    <rect x="54" y="144" width="128" height="9" fill="var(--grey)"/><rect x="54" y="153" width="282" height="9" fill="var(--teal)"/><rect x="54" y="162" width="160" height="9" fill="var(--navy)"/>
    <rect x="54" y="204" width="128" height="9" fill="var(--grey)"/><rect x="54" y="213" width="154" height="9" fill="var(--teal)"/><rect x="54" y="222" width="275" height="9" fill="var(--navy)"/>
    <g font-size="8" fill="#777" text-anchor="middle"><text x="54" y="260">0</text><text x="118" y="260">1</text><text x="182" y="260">2</text><text x="246" y="260">3</text><text x="310" y="260">4</text><text x="374" y="260">5</text><text x="438" y="260">6</text></g>
  </svg>
  <div class="legend-row" style="top:150px;color:var(--navy)"><h4>Title Goes Here!</h4><p>Lorem ipsum dolor sit amet, at laborum nibh duis mauris. Per ultrices lectus sed metus tristique eu. Diam suspendisse ac ipsum</p></div>
  <div class="legend-row" style="top:245px;color:var(--teal)"><h4>Title Goes Here!</h4><p>Lorem ipsum dolor sit amet, at laborum nibh duis mauris. Per ultrices lectus sed metus tristique eu. Diam suspendisse ac ipsum</p></div>
  <div class="legend-row" style="top:340px;color:var(--grey)"><h4>Title Goes Here!</h4><p>Lorem ipsum dolor sit amet, at laborum nibh duis mauris. Per ultrices lectus sed metus tristique eu. Diam suspendisse ac ipsum</p></div>
  <svg class="foot" viewBox="0 0 960 70"><polygon points="0,12 112,12 156,56 960,56 960,70 0,70" fill="url(#footGrad)"/></svg>
  <div class="foot-brand">Duvernet</div><div class="foot-copy">Copyright 2021 Duvernet Conseil. All rights reserved &nbsp;|&nbsp; 12</div>
</section>

<!-- Donuts -->
<section class="slide" style="left:52px;top:2670px">
  <div class="slide-title">Slide Title Goes Here!</div>
  <div class="donut" style="left:113px;top:140px">
    <svg width="200" height="200" viewBox="0 0 200 200"><circle cx="100" cy="100" r="88" fill="none" stroke="#e6e8ea" stroke-width="10"/><circle cx="100" cy="100" r="88" fill="none" stroke="var(--navy)" stroke-width="10" stroke-dasharray="354 553" transform="rotate(-90 100 100)"/></svg>
    <div class="donut-value" style="color:var(--navy)">64<span>%</span></div>
    <div class="donut-head">Heading</div><div class="donut-text">Lorem ipsum dolor sit amet, at laborum nibh duis mauris. Per ultrices lectus sed metus.</div>
  </div>
  <div class="donut" style="left:378px;top:140px">
    <svg width="200" height="200" viewBox="0 0 200 200"><circle cx="100" cy="100" r="88" fill="none" stroke="#e6e8ea" stroke-width="10"/><circle cx="100" cy="100" r="88" fill="none" stroke="var(--teal)" stroke-width="10" stroke-dasharray="453 553" transform="rotate(-90 100 100)"/></svg>
    <div class="donut-value" style="color:var(--teal)">82<span>%</span></div>
    <div class="donut-head" style="color:var(--teal)">Heading</div><div class="donut-text">Lorem ipsum dolor sit amet, at laborum nibh duis mauris. Per ultrices lectus sed metus.</div>
  </div>
  <div class="donut" style="left:644px;top:140px">
    <svg width="200" height="200" viewBox="0 0 200 200"><circle cx="100" cy="100" r="88" fill="none" stroke="#e6e8ea" stroke-width="10"/><circle cx="100" cy="100" r="88" fill="none" stroke="var(--grey)" stroke-width="10" stroke-dasharray="520 553" transform="rotate(-90 100 100)"/></svg>
    <div class="donut-value" style="color:var(--grey)">94<span>%</span></div>
    <div class="donut-head">Heading</div><div class="donut-text">Lorem ipsum dolor sit amet, at laborum nibh duis mauris. Per ultrices lectus sed metus.</div>
  </div>
  <svg class="foot" viewBox="0 0 960 70"><polygon points="0,12 112,12 156,56 960,56 960,70 0,70" fill="url(#footGrad)"/></svg>
  <div class="foot-brand">Duvernet</div><div class="foot-copy">Copyright 2021 Duvernet Conseil. All rights reserved &nbsp;|&nbsp; 13</div>
</section>

<!-- Table -->
<section class="slide" style="left:610px;top:2670px">
  <div class="slide-title">Slide Title Goes Here!</div>
  <table class="grid-table">
    <tr><th>Heading</th><th>Title 1</th><th>Title 2</th><th>Title 3</th><th>Title 4</th></tr>
    <tr><td>Lorem ipsum dolor</td><td>203</td><td>678</td><td>566</td><td>788</td></tr>
    <tr><td>Lorem ipsum dolor</td><td>456</td><td>874</td><td>333</td><td>566</td></tr>
    <tr><td>Lorem ipsum dolor</td><td>675</td><td>456</td><td>256</td><td>344</td></tr>
    <tr><td>Lorem ipsum dolor</td><td>123</td><td>345</td><td>345</td><td>233</td></tr>
    <tr><td>Lorem ipsum dolor</td><td>456</td><td>122</td><td>123</td><td>455</td></tr>
  </table>
  <svg class="foot" viewBox="0 0 960 70"><polygon points="0,12 112,12 156,56 960,56 960,70 0,70" fill="url(#footGrad)"/></svg>
  <div class="foot-brand">Duvernet</div><div class="foot-copy">Copyright 2021 Duvernet Conseil. All rights reserved &nbsp;|&nbsp; 14</div>
</section>

<!-- Closing -->
<section class="slide" style="left:330px;top:2993px">
  <svg class="fill" viewBox="0 0 960 540"><defs><linearGradient id="closeGrad" x1="0" y1="0" x2="0" y2="1"><stop offset="0" stop-color="#0f8795"/><stop offset="1" stop-color="#0a3d5a"/></linearGradient></defs><rect role="img" aria-label="Photo of hands at a desk, tinted deep teal" width="960" height="540" fill="url(#closeGrad)"/></svg>
  <div class="brand" style="left:190px;top:200px;width:300px;font-size:28px;color:#fff">Duvernet<small>CONSEIL</small></div>
  <div class="abs" style="left:510px;top:205px;width:2px;height:170px;background:rgba(255,255,255,.6)"></div>
  <div class="contact">
    <h3>Contact Us</h3>
    <p><svg viewBox="0 0 24 24"><path d="M6 2h4l2 5-3 2a12 12 0 0 0 6 6l2-3 5 2v4a2 2 0 0 1-2 2A18 18 0 0 1 4 4a2 2 0 0 1 2-2z" fill="#fff"/></svg>555-0142-7788</p>
    <p><svg viewBox="0 0 24 24"><circle cx="12" cy="12" r="9" fill="none" stroke="#fff" stroke-width="2.5"/><circle cx="12" cy="12" r="3.5" fill="none" stroke="#fff" stroke-width="2.5"/></svg>info@duvernet-conseil.com</p>
    <p><svg viewBox="0 0 24 24"><circle cx="12" cy="12" r="9" fill="none" stroke="#fff" stroke-width="2"/><ellipse cx="12" cy="12" rx="4" ry="9" fill="none" stroke="#fff" stroke-width="2"/><line x1="3" y1="12" x2="21" y2="12" stroke="#fff" stroke-width="2"/></svg>www.duvernet-conseil.com</p>
  </div>
</section>

</body>
</html>
```